Real Estate Company Looking for Business Card Designs for 3 Executives

Hello!
Thanks so much for considering our project! We are a real estate investment company located in Edmonton, Alberta called Marlbeck Group of Companies. We invest/develop both commercial and residential real estate and are looking to create 3 DOUBLE-SIDED business cards for 3 top executives in the company! (for some reason it won't let us select the double-sided option, but yes, the cards are double sided and would be happy to tip extra)

We have certain guidelines that we want our business cards to for sure follow - the back of the Business card has to be the Black Background Version of the Logo which has already been designed and linked as a file (first file). We want the entire back of the card to simply just be the black background logo. In terms of the front of the card, would like to see a smaller version of the white background logo (linked as the second file) in the top left hand corner - of course, feel free to get creative and we can make revisions together along the way! and Then after that, just text. We want the card to be sharp, clean, easy on the eyes and highly professional looking. We would like the card to include the Full name of the Company (Marlbeck Group of Companies), Name of the Person, Title, Phone, Email. If possible please provide the front part of the card for 3 people:

1) Marlbeck Group of Companies, Lena Okafor, Chief Financial Officer, 780-555-0162, lenaokafor@marlbeckgroup.example

2) Marlbeck Group of Companies, Tobias Okafor, Chief Executive Officer, 780-555-0148, tobiasokafor@marlbeckgroup.example

3) Marlbeck Group of Companies, Rui Dalton, Chief Operations Officer, 587-555-0193, ruidalton@marlbeckgroup.example

Thank you so much for considering our project & we look forward to seeing your designs!

```html
<!DOCTYPE html>
<html lang="en">
<head>
<meta charset="utf-8">
<title>Marlbeck Business Cards</title>
<link href="https://fonts.googleapis.com/css2?family=Arimo:wght@400;700&display=swap" rel="stylesheet">
<style>
  :root {
    --backdrop: #e4e4e4;
    --card-black: #0b0809;
    --card-white: #f7f7f7;
    --ink: #111111;
    --ink-soft: #2a2a2a;
    --logo-white: #f3f8f8;
  }
  * { box-sizing: border-box; margin: 0; padding: 0; }
  html, body {
    width: 1200px;
    height: 930px;
    overflow: hidden;
    background: var(--backdrop);
    font-family: "Arimo", Arial, sans-serif;
  }
  .canvas {
    position: relative;
    width: 1200px;
    height: 930px;
  }
  .card {
    position: absolute;
    width: 560px;
    height: 320px;
    box-shadow: 0 10px 26px rgba(0,0,0,0.14);
    overflow: hidden;
  }
  .card--back {
    left: 580px;
    top: 110px;
    background: var(--card-black);
    display: flex;
    align-items: center;
    justify-content: center;
  }
  .card--front {
    left: 70px;
    top: 500px;
    display: flex;
    background: var(--card-white);
  }
  .brand-mark {
    color: var(--logo-white);
    font-weight: 400;
    letter-spacing: 0.42em;
    text-transform: uppercase;
    padding-left: 0.42em;
  }
  .card--back .brand-mark { font-size: 30px; }
  .front__logo-panel {
    width: 50%;
    background: var(--card-black);
    display: flex;
    align-items: center;
    justify-content: center;
  }
  .front__logo-panel .brand-mark { font-size: 19px; }
  .front__details {
    width: 50%;
    padding: 58px 0 0 30px;
    color: var(--ink);
  }
  .person__name {
    font-size: 17px;
    font-weight: 700;
    text-transform: uppercase;
    letter-spacing: 0.02em;
  }
  .person__title {
    font-size: 14px;
    color: var(--ink-soft);
    margin-top: 2px;
  }
  .contact-list {
    list-style: none;
    margin-top: 22px;
  }
  .contact-list li {
    display: flex;
    align-items: center;
    gap: 7px;
    font-size: 13.5px;
    line-height: 1.55;
    white-space: nowrap;
  }
  .contact-icon {
    width: 12px;
    height: 12px;
    flex: none;
  }
</style>
</head>
<body>
  <main class="canvas">
    <section class="card card--back" aria-label="Card back">
      <span class="brand-mark">Marlbeck</span>
    </section>

    <section class="card card--front" aria-label="Card front">
      <div class="front__logo-panel">
        <span class="brand-mark">Marlbeck</span>
      </div>
      <div class="front__details">
        <h1 class="person__name">Lena Okafor</h1>
        <p class="person__title">Chief Financial Officer</p>
        <ul class="contact-list">
          <li>
            <svg class="contact-icon" viewBox="0 0 24 24" aria-hidden="true">
              <path fill="#111" d="M6.6 10.8a15.1 15.1 0 0 0 6.6 6.6l2.2-2.2a1 1 0 0 1 1-.25 11.4 11.4 0 0 0 3.6.57 1 1 0 0 1 1 1V20a1 1 0 0 1-1 1A17 17 0 0 1 3 4a1 1 0 0 1 1-1h3.5a1 1 0 0 1 1 1c0 1.25.2 2.45.57 3.57a1 1 0 0 1-.25 1z"/>
            </svg>
            780-555-0162
          </li>
          <li>
            <svg class="contact-icon" viewBox="0 0 24 24" aria-hidden="true">
              <rect x="2" y="5" width="20" height="14" fill="#111"/>
              <path d="M2 5l10 8 10-8" fill="none" stroke="#f7f7f7" stroke-width="1.6"/>
            </svg>
            lenaokafor@marlbeckgroup.example
          </li>
          <li>
            <svg class="contact-icon" viewBox="0 0 24 24" aria-hidden="true">
              <circle cx="12" cy="12" r="10" fill="#111"/>
              <g fill="none" stroke="#f7f7f7" stroke-width="1.3">
                <ellipse cx="12" cy="12" rx="4" ry="10"/>
                <line x1="2" y1="12" x2="22" y2="12"/>
                <line x1="4" y1="7" x2="20" y2="7"/>
                <line x1="4" y1="17" x2="20" y2="17"/>
              </g>
            </svg>
            www.marlbeckgroup.example
          </li>
        </ul>
      </div>
    </section>
  </main>
</body>
</html>
```